Presentation Flyer for Married Couple at night separate business owners by day

I would like a flyer to use to advertise free presentations put on by husband and I. I (Renata Volkhaven) am an estate planning attorney that works for PWR Law. My husband (Dan Volkhaven) is a financial planner that works for Quelmora Financial Planning. Would love it to be funny but serious. At night we are a married couple of 4 children, by day we individually work with people helping them protect their assets and their families.
Goal is for this to be used for multiple events.
Things to include: Food will be provided, Raffle for $500 off an Estate Plan Package
Topics to be covered in Seminar:
Estate & Financial Planning Essentials

Protect Your Future
Build a strong financial foundation with emergency funds, retirement planning, and smart investment strategies that match your goals.

Secure Your Legacy
Learn about wills, trusts, and powers of attorney - the essential documents everyone needs to protect their family's future.

Guard Your Assets
Understand the right insurance coverage to protect yourself and your loved ones, from life insurance to long-term care options.

Transfer Wealth Wisely
Discover tax-efficient strategies for passing assets to the next generation and making the most of your charitable giving.

```html
<!DOCTYPE html>
<html lang="en">
<head>
<meta charset="utf-8">
<title>Estate &amp; Financial Planning Seminar Flyer</title>
<link rel="stylesheet" href="https://fonts.googleapis.com/css2?family=Cinzel:wght@600;700;800&family=Poppins:wght@400;600;700&family=Montserrat:wght@500&display=swap">
<style>
  :root {
    --teal: #1b6f6e;
    --navy: #0d3f7d;
    --ink: #151515;
    --paper: #ffffff;
  }
  * { margin: 0; padding: 0; box-sizing: border-box; }
  html, body { width: 990px; height: 1200px; overflow: hidden; background: var(--paper); }
  .flyer {
    position: relative; width: 990px; height: 1200px; overflow: hidden;
    background: radial-gradient(ellipse at 75% 40%, #f1f2f3 0%, var(--paper) 60%);
    font-family: "Poppins", sans-serif; color: var(--ink);
  }
  .tag {
    position: absolute; left: 67px; width: 210px; height: 36px;
    background: var(--teal); color: #fff;
    border-radius: 0 20px 20px 0; border-left: 4px solid var(--paper);
    box-shadow: -7px 0 0 var(--teal); margin-left: 7px;
    font-family: "Cinzel", serif; font-weight: 700; font-size: 29px;
    letter-spacing: 2px; line-height: 36px; padding-left: 16px;
  }
  .tag-night { top: 57px; }
  .tag-day { top: 235px; }
  .headline { position: absolute; left: 64px; font-family: "Cinzel", serif; font-weight: 700; line-height: 1; white-space: nowrap; }
  .h-married { top: 100px; font-size: 66px; color: var(--teal); letter-spacing: 1px; }
  .h-couple { top: 160px; font-size: 66px; color: var(--ink); letter-spacing: 1px; }
  .h-your { top: 284px; font-size: 34px; color: var(--ink); left: 70px; }
  .h-estate { top: 319px; font-size: 68px; color: var(--teal); }
  .h-financial { top: 377px; font-size: 68px; color: var(--teal); }
  .h-experts { top: 438px; font-size: 35px; color: var(--ink); }

  .brand { position: absolute; font-family: "Poppins", sans-serif; font-weight: 600; color: var(--ink); white-space: nowrap; }
  .brand-law { left: 556px; top: 86px; font-size: 27px; line-height: 34px; }
  .brand-fin { left: 752px; top: 84px; font-size: 16px; line-height: 20px; }

  .badge {
    position: absolute; left: 539px; top: 182px; width: 324px; height: 94px;
    border: 2px solid var(--teal); border-radius: 14px; overflow: hidden; display: flex; background: #fff;
  }
  .badge-main { width: 165px; background: var(--teal); color: #fff; text-align: center; padding-top: 8px; }
  .badge-free { font-family: "Cinzel", serif; font-weight: 800; font-size: 44px; line-height: 44px; }
  .badge-seminar { font-weight: 700; font-size: 28px; line-height: 32px; }
  .badge-perks { padding: 12px 0 0 15px; font-weight: 700; font-size: 12.5px; line-height: 15px; }

  .intro {
    position: absolute; left: 543px; top: 300px; width: 340px;
    border-left: 2px solid var(--navy); padding-left: 12px;
    font-size: 15.4px; line-height: 18.4px;
  }
  .intro strong { font-weight: 700; }

  .portrait {
    position: absolute; left: 428px; top: 486px; width: 562px; height: 714px;
    background: linear-gradient(90deg, rgba(255,255,255,0) 0%, #8d8d8d 22%, #3a3a3a 55%, #2a2a2a 100%);
    -webkit-mask: linear-gradient(180deg, transparent 0%, #000 18%);
            mask: linear-gradient(180deg, transparent 0%, #000 18%);
  }

  .topics-label {
    position: absolute; left: 66px; top: 1034px; transform-origin: 0 0; transform: rotate(-90deg);
    font-family: "Cinzel", serif; font-weight: 600; font-size: 37px; letter-spacing: 7px; white-space: nowrap; line-height: 36px;
  }
  .topic {
    position: absolute; width: 169px; height: 216px; border-radius: 10px; color: #fff; text-align: center;
    padding: 32px 16px 0;
  }
  .topic.teal { background: var(--teal); }
  .topic.navy { background: var(--navy); }
  .topic h3 { font-family: "Cinzel", serif; font-weight: 700; font-size: 13.5px; line-height: 15px; margin-bottom: 7px; }
  .topic p { font-size: 12.6px; line-height: 15.2px; }
  .topic .tick { position: absolute; left: 69px; top: -17px; }
  .t1 { left: 119px; top: 544px; }
  .t2 { left: 298px; top: 544px; }
  .t3 { left: 119px; top: 805px; }
  .t4 { left: 298px; top: 805px; }

  .cta { position: absolute; left: 71px; top: 1062px; font-family: "Cinzel", serif; font-weight: 700; font-size: 25px; color: var(--teal); white-space: nowrap; }
  .cta .today { color: var(--navy); }
  .links { position: absolute; left: 71px; top: 1101px; list-style: none; font-family: "Montserrat", sans-serif; font-weight: 500; font-size: 15.5px; letter-spacing: 2.3px; line-height: 24px; }
  .links li { display: flex; align-items: center; gap: 4px; }
</style>
</head>
<body>
<main class="flyer">
  <div class="tag tag-night">By Night</div>
  <h1>
    <span class="headline h-married">A Married</span>
    <span class="headline h-couple">Couple</span>
  </h1>
  <div class="tag tag-day">By Day</div>
  <h2>
    <span class="headline h-your">Your</span>
    <span class="headline h-estate">Estate &amp;</span>
    <span class="headline h-financial">Financial</span>
    <span class="headline h-experts">Planning Experts</span>
  </h2>

  <div class="brand brand-law">PWR Law</div>
  <div class="brand brand-fin">Quelmora Financial<br>Planning</div>

  <div class="badge">
    <div class="badge-main">
      <div class="badge-free">FREE</div>
      <div class="badge-seminar">Seminar</div>
    </div>
    <div class="badge-perks">Food Provided<br>+<br>Raffle for $500 Off<br>an Estate Plan<br>Package!</div>
  </div>

  <p class="intro"><strong>Renata Volkhaven, Estate Planning Attorney at PWR Law,</strong> and <strong>Dan Volkhaven, Financial Planner at Quelmora Financial Planning,</strong> for an informative (and slightly entertaining) evening designed to help you protect your future, secure your legacy, and guard your assets.</p>

  <div class="portrait" role="img" aria-label="Black and white portrait of the married couple, the attorney and the financial planner, seated side by side and smiling"></div>

  <div class="topics-label">Topics We’ll Cover</div>

  <section class="topic teal t1">
    <svg class="tick" width="32" height="32" viewBox="0 0 32 32" aria-hidden="true"><circle cx="16" cy="16" r="14" fill="#fff" stroke="#151515" stroke-width="2"/><path d="M10 16.5l4 4 8-8" fill="none" stroke="#151515" stroke-width="2.6" stroke-linecap="round" stroke-linejoin="round"/></svg>
    <h3>Protect Your Future</h3>
    <p>Build a strong financial foundation with emergency funds, retirement planning, and smart investment strategies that match your goals.</p>
  </section>
  <section class="topic navy t2">
    <svg class="tick" width="32" height="32" viewBox="0 0 32 32" aria-hidden="true"><circle cx="16" cy="16" r="14" fill="#fff" stroke="#151515" stroke-width="2"/><path d="M10 16.5l4 4 8-8" fill="none" stroke="#151515" stroke-width="2.6" stroke-linecap="round" stroke-linejoin="round"/></svg>
    <h3>Secure Your Legacy</h3>
    <p>Learn about wills, trusts, and powers of attorney - the essential documents everyone needs to protect their family's future.</p>
  </section>
  <section class="topic navy t3">
    <svg class="tick" width="32" height="32" viewBox="0 0 32 32" aria-hidden="true"><circle cx="16" cy="16" r="14" fill="#fff" stroke="#151515" stroke-width="2"/><path d="M10 16.5l4 4 8-8" fill="none" stroke="#151515" stroke-width="2.6" stroke-linecap="round" stroke-linejoin="round"/></svg>
    <h3>Guard Your Assets</h3>
    <p>Understand the right insurance coverage to protect yourself and your loved ones, from life insurance to long-term care options.</p>
  </section>
  <section class="topic teal t4">
    <svg class="tick" width="32" height="32" viewBox="0 0 32 32" aria-hidden="true"><circle cx="16" cy="16" r="14" fill="#fff" stroke="#151515" stroke-width="2"/><path d="M10 16.5l4 4 8-8" fill="none" stroke="#151515" stroke-width="2.6" stroke-linecap="round" stroke-linejoin="round"/></svg>
    <h3>Transfer Wealth Wisely</h3>
    <p>Discover tax-efficient strategies for passing assets to the next generation and making the most of your charitable giving.</p>
  </section>

  <div class="cta">Reserve Your <span class="today">Spot Today</span></div>
  <ul class="links">
    <li><svg width="16" height="16" viewBox="0 0 16 16" aria-hidden="true"><circle cx="8" cy="8" r="7" fill="none" stroke="#0d3f7d" stroke-width="1.6"/><path d="M1 8h14M8 1c-3 3.5-3 10.5 0 14M8 1c3 3.5 3 10.5 0 14" fill="none" stroke="#0d3f7d" stroke-width="1.2"/></svg>www.guardandbuildwealth.com</li>
    <li><svg width="16" height="16" viewBox="0 0 16 16" aria-hidden="true"><circle cx="8" cy="8" r="7" fill="none" stroke="#0d3f7d" stroke-width="1.6"/><path d="M1 8h14M8 1c-3 3.5-3 10.5 0 14M8 1c3 3.5 3 10.5 0 14" fill="none" stroke="#0d3f7d" stroke-width="1.2"/></svg>www.pwrlawoffice.com</li>
  </ul>
</main>
</body>
</html>
```